Modern, Clean, Edgy & Fun Comedy Show Flyer

We need to a create a new flyer for the comedy show, Harbor Laugh Night. The original version of the flyer is attached (file: Old flyer), as well as two versions of the logo.
- The text should be the same except now the show is Every First Wednesday and the next show is June 1.
- Remove the jerk shop logo
- Remove the picture of the man, and replace it with a photo of Delphine (our host), the Audience, or something of your own design.
* pictures of Delphine and the Audience is attached.
* We'd like to keep the same color palette and have also attached a color palette for reference

I have also attached 4 references of flyers that I like, that you can use to get an idea of the theme and aesthetic we are looking for.
* Files: Reference 1, Reference 2, Reference 3, Reference 4
Updates

Colors
3277b5
85acd3
0455a3
eaf1f7
cee9f5
ecf7fb
d5d5d5
e6e6e6

Requirements
Must have
• The harbor laugh night logo attached
• The text as specified in the project description
• An option with Delphine and without

```html
<!DOCTYPE html>
<html lang="en">
<head>
<meta charset="utf-8">
<title>Harbor Laugh Night – Free Comedy Show</title>
<link rel="stylesheet" href="https://fonts.googleapis.com/css2?family=Allerta+Stencil&family=Roboto+Slab:wght@800&family=Oswald:wght@600&family=Roboto:wght@700&family=Archivo+Black&display=swap">
<style>
  :root {
    --blue-deep: #0455a3;
    --blue-bright: #1d5fd6;
    --blue-mid: #3277b5;
    --blue-soft: #85acd3;
    --white: #ffffff;
    --ink: #111111;
    --grey-text: #8a8a8a;
  }
  * { margin: 0; padding: 0; box-sizing: border-box; }
  html, body { width: 1200px; height: 929px; overflow: hidden; background: var(--white); }
  .flyer { position: relative; width: 1200px; height: 929px; overflow: hidden; background: var(--white); }

  .stage-photo {
    position: absolute; left: 0; top: 0; width: 1200px; height: 720px;
    background:
      radial-gradient(ellipse 90px 70px at 235px 100px, rgba(255,245,225,.55), transparent 75%),
      radial-gradient(ellipse 140px 200px at 225px 330px, rgba(120,70,190,.55), transparent 72%),
      radial-gradient(ellipse 140px 90px at 85px 450px, rgba(40,60,190,.85), transparent 78%),
      radial-gradient(ellipse 80px 60px at 70px 330px, rgba(70,150,220,.45), transparent 75%),
      radial-gradient(ellipse 110px 120px at 370px 310px, rgba(150,75,45,.55), transparent 75%),
      radial-gradient(ellipse 60px 90px at 565px 350px, rgba(210,150,60,.55), transparent 78%),
      radial-gradient(ellipse 170px 90px at 700px 380px, rgba(185,120,55,.45), transparent 78%),
      radial-gradient(ellipse 260px 40px at 820px 215px, rgba(230,170,90,.25), transparent 80%),
      radial-gradient(ellipse 300px 160px at 1000px 470px, rgba(70,55,60,.55), transparent 80%),
      radial-gradient(ellipse 260px 120px at 250px 600px, rgba(95,70,50,.55), transparent 80%),
      radial-gradient(ellipse 90px 60px at 535px 540px, rgba(110,110,115,.55), transparent 80%),
      linear-gradient(180deg, #0e0b0a 0%, #241a15 30%, #3b2a1f 55%, #1c1612 80%, #120f0d 100%);
  }
  .white-edge { position: absolute; left: 0; top: 480px; width: 1200px; height: 260px; }

  .headline {
    position: absolute; top: 24px; left: 0; width: 1200px; text-align: center;
    font-family: "Allerta Stencil", sans-serif; font-size: 43px; letter-spacing: 2px;
    color: var(--blue-soft);
  }

  .lineup { position: absolute; left: 710px; top: 176px; width: 400px; text-align: center; }
  .lineup-label {
    font-family: "Archivo Black", sans-serif; font-size: 20px; color: var(--blue-bright);
    margin-bottom: 14px;
  }
  .lineup-name {
    font-family: "Roboto Slab", serif; font-weight: 800; font-size: 24px;
    letter-spacing: 1px; line-height: 49px; color: var(--white); white-space: nowrap;
  }
  .lineup-name.alt { color: var(--blue-soft); }

  .show-details { position: absolute; left: 40px; top: 756px; width: 290px; text-align: center; }
  .show-date {
    font-family: "Allerta Stencil", sans-serif; font-size: 27px; color: var(--blue-deep);
    letter-spacing: 1px; margin-bottom: 6px;
  }
  .venue { font-family: "Roboto", sans-serif; font-weight: 700; font-size: 19px; color: var(--ink); line-height: 28px; }
  .venue-info { font-family: "Roboto", sans-serif; font-weight: 700; font-size: 20px; color: var(--grey-text); line-height: 29px; white-space: nowrap; }

  .host { position: absolute; left: 434px; top: 678px; width: 230px; text-align: center; }
  .host-label {
    font-family: "Allerta Stencil", sans-serif; font-size: 25px; color: var(--blue-soft);
    letter-spacing: 1px; margin-bottom: 3px;
  }
  .host-portrait {
    width: 172px; height: 130px; margin: 0 auto; border: 3px solid var(--blue-deep);
    background: linear-gradient(180deg, #f2ece8 0%, #6b4b3e 100%);
  }
  .host-name {
    margin-top: 6px; height: 44px; background: var(--blue-deep); color: var(--white);
    font-family: "Oswald", sans-serif; font-weight: 600; font-size: 22px; line-height: 44px;
    letter-spacing: .5px; white-space: nowrap;
  }

  .show-name {
    position: absolute; left: 715px; top: 700px; width: 460px; text-align: center;
    font-family: "Allerta Stencil", sans-serif; font-size: 58px; line-height: 72px;
    color: var(--blue-bright);
  }
</style>
</head>
<body>
<main class="flyer">
  <div class="stage-photo" role="img" aria-label="Photo of a comedian performing on a dim brick-walled stage with a DJ table and a seated audience"></div>

  <svg class="white-edge" viewBox="0 0 1200 260" preserveAspectRatio="none" aria-hidden="true">
    <path d="M0 190 L60 175 L110 182 L170 160 L230 172 L290 150 L350 162 L420 130 L480 140 L540 110 L600 118 L660 92 L720 100 L790 76 L850 82 L910 60 L970 66 L1030 44 L1090 50 L1150 30 L1200 34 L1200 260 L0 260 Z" fill="var(--blue-mid)"/>
    <path d="M0 205 L50 196 L100 204 L160 184 L220 194 L280 176 L340 186 L400 160 L470 168 L530 140 L590 146 L650 120 L720 126 L780 104 L850 110 L910 90 L970 94 L1040 74 L1100 80 L1160 62 L1200 66 L1200 260 L0 260 Z" fill="var(--white)"/>
  </svg>

  <h1 class="headline">FREE COMEDY SHOW EVERY FIRST WEDNESDAY</h1>

  <section class="lineup">
    <p class="lineup-label">FEATURING</p>
    <p class="lineup-name">WARREN HOLLOWAY</p>
    <p class="lineup-name alt">THEO MARSH</p>
    <p class="lineup-name">FELIX BERGMANN-LOWE</p>
    <p class="lineup-name alt">RAVI DESAI</p>
    <p class="lineup-name">TESSA OKAFOR</p>
  </section>

  <section class="show-details">
    <p class="show-date">WED. JUNE 1</p>
    <p class="venue">The Ink Crate</p>
    <p class="venue-info">84 Tidewater Lane, Harborview</p>
    <p class="venue-info">Doors 6:30 PM</p>
  </section>

  <section class="host">
    <p class="host-label">HOSTED BY</p>
    <div class="host-portrait" role="img" aria-label="Portrait photo of the host, Delphine Ashworth"></div>
    <p class="host-name">DELPHINE ASHWORTH</p>
  </section>

  <p class="show-name">Harbor<br>Laugh Night</p>
</main>
</body>
</html>
```